Private Medical Clinic needs a letterhead design

Letterhead that can be edited. Letter head is needed for printing official doctor's notes, referrals, etc in a medical clinic. The letterhead should use the attached logos

```html
<!DOCTYPE html>
<html lang="en">
<head>
<meta charset="utf-8">
<title>Tall Cedar Family Medicine – Letterhead</title>
<link href="https://fonts.googleapis.com/css2?family=Open+Sans:wght@400&family=Roboto:wght@400&display=swap" rel="stylesheet">
<style>
  :root {
    --backdrop: #e6e6e6;
    --paper: #f5f5f4;
    --ink: #3f3f3f;
    --ink-soft: #5a5a5a;
    --band: #4b514a;
    --signature-tone: #dcdcdc;
  }
  * { margin: 0; padding: 0; box-sizing: border-box; }
  html, body {
    width: 1200px; height: 795px; overflow: hidden;
    background: var(--backdrop);
  }
  body { display: flex; align-items: center; justify-content: center; }
  .letterhead {
    position: relative;
    width: 536px; height: 758px;
    background: var(--paper);
    box-shadow: 0 2px 10px rgba(0,0,0,0.12);
    font-family: "Open Sans", sans-serif;
    color: var(--ink-soft);
  }
  .brand {
    position: absolute; left: 46px; top: 62px;
    display: flex; align-items: center; gap: 8px;
    font-family: "Open Sans", sans-serif;
    font-size: 15px; color: var(--ink);
  }
  .brand-dot {
    width: 14px; height: 14px; border-radius: 50%;
    background: var(--ink);
  }
  .contact {
    position: absolute; left: 372px; top: 40px;
    list-style: none;
    font-family: "Roboto", sans-serif;
    font-size: 10.5px; line-height: 13px; color: var(--ink);
  }
  .contact li { display: flex; align-items: center; gap: 5px; }
  .contact svg { width: 8px; height: 8px; fill: var(--ink); }
  .letter-body {
    position: absolute; left: 72px; top: 150px; width: 420px;
    font-size: 10px; line-height: 14px;
  }
  .salutation { margin-bottom: 14px; }
  .letter-body p.paragraph { margin-bottom: 14px; }
  .closing { margin-top: 6px; }
  .signature {
    position: absolute; left: 110px; top: 560px;
    width: 110px; height: 56px;
    background: var(--signature-tone); border-radius: 4px;
  }
  .address {
    position: absolute; right: 44px; bottom: 30px;
    display: flex; align-items: center; gap: 5px;
    font-family: "Roboto", sans-serif;
    font-size: 12px; color: var(--ink);
  }
  .address svg { width: 9px; height: 12px; fill: var(--ink); }
  .footer-band {
    position: absolute; left: 0; right: 0; bottom: 0;
    height: 7px; background: var(--band);
  }
</style>
</head>
<body>
  <main class="letterhead">
    <div class="brand">
      <span class="brand-dot"></span>
      <span class="brand-name">Tall Cedar Family Medicine</span>
    </div>

    <ul class="contact">
      <li><svg viewBox="0 0 10 10"><path d="M2 1l2 2-1 1.2c.6 1.2 1.6 2.2 2.8 2.8L7 6l2 2-1.5 1.5C4 9 1 6 .5 2.5z"/></svg>555.014.2200</li>
      <li><svg viewBox="0 0 10 10"><rect x="2.5" y="0.5" width="5" height="3"/><rect x="0.5" y="3.5" width="9" height="4" rx="1"/><rect x="2.5" y="7" width="5" height="2.5"/></svg>555.014.2291</li>
      <li><svg viewBox="0 0 10 10"><path d="M0 2h10v6H0z M0 2l5 3.5L10 2" stroke="#f5f5f4" stroke-width="0.8"/></svg>office@tallcedarclinic.com</li>
      <li><svg viewBox="0 0 10 10"><circle cx="5" cy="5" r="4.5"/></svg>www.tallcedarclinic.com</li>
    </ul>

    <section class="letter-body">
      <p class="salutation">Dear customer,</p>
      <p class="paragraph">Lorem ipsum dolor sit amet, consectetur adipisicing elit, sed do eiusmod tempor incididunt ut labore et dolore magna aliqua. Ut enim ad minim veniam, quis nostrud exercitation ullamco laboris nisi ut aliquip ex ea commodo consequat. Duis aute irure dolor in reprehenderit in voluptate velit esse cillum dolore eu fugiat nulla pariatur. Excepteur sint occaecat cupidatat non proident, sunt in culpa qui officia deserunt mollit anim id est laborum.</p>
      <p class="paragraph">Lorem ipsum dolor sit amet, consectetur adipisicing elit, sed do eiusmod tempor incididunt ut labore et dolore magna aliqua. Ut enim ad minim veniam, quis nostrud exercitation ullamco laboris nisi ut aliquip ex ea commodo consequat. Duis aute irure dolor in reprehenderit in voluptate velit esse cillum dolore eu fugiat nulla pariatur. Excepteur sint occaecat cupidatat non proident, sunt in culpa qui officia deserunt mollit anim id est laborum.</p>
      <p class="paragraph">Lorem ipsum dolor sit amet, consectetur adipisicing elit, sed do eiusmod tempor incididunt ut labore et dolore magna aliqua. Ut enim ad minim veniam, quis nostrud exercitation ullamco laboris nisi ut aliquip ex ea commodo consequat. Duis aute irure dolor in reprehenderit in voluptate velit esse cillum dolore eu fugiat nulla pariatur. Excepteur sint occaecat cupidatat non proident, sunt in culpa qui officia deserunt mollit anim id est laborum.</p>
      <p class="paragraph">Lorem ipsum dolor sit amet, consectetur adipisicing elit, sed do eiusmod tempor incididunt ut labore et dolore magna aliqua. Ut enim ad minim veniam, quis nostrud exercitation ullamco laboris nisi ut aliquip ex ea commodo consequat. Duis aute irure dolor in reprehenderit.</p>
      <p class="closing">Yours Sincerely,</p>
    </section>

    <div class="signature" role="img" aria-label="Handwritten signature of the physician"></div>

    <div class="address">
      <svg viewBox="0 0 9 12"><path d="M4.5 0A4.5 4.5 0 0 0 0 4.5C0 8 4.5 12 4.5 12S9 8 9 4.5A4.5 4.5 0 0 0 4.5 0zm0 6.3a1.8 1.8 0 1 1 0-3.6 1.8 1.8 0 0 1 0 3.6z"/></svg>
      48 Linden Ave., Halton ON Canada L7A2B3
    </div>

    <div class="footer-band"></div>
  </main>
</body>
</html>
```